New company documents design

Hi Kip,
We are looking for new versions of the below and would like these all be the in the same theme / style. The product data sheets with the company logo in the top left and the footer with the green highting over the website works well. Can this style be applied to the below:
- Business cards, w/QR code function
- Blank Letter Head
- Blank power point
- Blank Document (example attached, WHS-FRM)
- Email signature
- Corporate profile (copy attached)

```html
<!DOCTYPE html>
<html lang="en">
<head>
<meta charset="utf-8">
<title>Vertex Works Letterhead</title>
<link href="https://fonts.googleapis.com/css2?family=Open+Sans:wght@400;600;700&display=swap" rel="stylesheet">
<style>
  :root {
    --brand-blue: #0a2f9e;
    --brand-green: #079b2a;
    --text-grey: #7a7a7a;
    --text-dark: #3c3c3c;
    --sign-blue: #1d8fd6;
    --paper: #fcfcfc;
    --backdrop: #e9e9e9;
  }
  html, body {
    margin: 0;
    padding: 0;
    width: 1200px;
    height: 1200px;
    overflow: hidden;
    background: var(--backdrop);
    font-family: "Open Sans", sans-serif;
  }
  .letterhead {
    position: absolute;
    left: 197px;
    top: 30px;
    width: 806px;
    height: 1140px;
    background: var(--paper);
    box-shadow: 0 2px 10px rgba(0,0,0,0.12);
    overflow: hidden;
  }
  .brand {
    position: absolute;
    left: 81px;
    top: 80px;
    display: flex;
    align-items: center;
    gap: 12px;
  }
  .brand-square {
    width: 40px;
    height: 40px;
    background: var(--brand-blue);
  }
  .brand-name {
    font-weight: 700;
    font-size: 30px;
    letter-spacing: 1px;
    color: var(--brand-blue);
    line-height: 1;
  }
  .salutation {
    position: absolute;
    left: 81px;
    top: 277px;
    margin: 0;
    font-size: 12px;
    color: var(--text-grey);
  }
  .body-text {
    position: absolute;
    left: 81px;
    width: 645px;
    margin: 0;
    font-size: 11.8px;
    line-height: 20.4px;
    color: var(--text-grey);
    text-align: justify;
  }
  .p1 { top: 339px; }
  .p2 { top: 482px; }
  .p3 { top: 626px; }
  .sign-name {
    position: absolute;
    left: 81px;
    top: 770px;
    margin: 0;
    font-size: 12px;
    font-weight: 700;
    color: var(--text-grey);
  }
  .signature {
    position: absolute;
    left: 81px;
    top: 806px;
    width: 195px;
    height: 42px;
    background: linear-gradient(90deg, rgba(29,143,214,0.18), rgba(29,143,214,0.06));
    border-radius: 4px;
  }
  .sign-role {
    position: absolute;
    left: 81px;
    top: 852px;
    margin: 0;
    font-size: 12px;
    color: var(--text-grey);
  }
  .contact {
    position: absolute;
    left: 44px;
    top: 1052px;
    font-size: 14.5px;
    color: var(--text-dark);
  }
  .contact p { margin: 0 0 6px; }
  .contact-line {
    display: flex;
    align-items: center;
    gap: 6px;
  }
  .contact-line svg { flex: none; }
  .contact-line .gap { width: 10px; }
  .footer-band {
    position: absolute;
    left: 0;
    bottom: 0;
    width: 100%;
    height: 15px;
    background: var(--brand-green);
  }
  .footer-web {
    position: absolute;
    right: 0;
    bottom: 0;
    width: 280px;
    height: 36px;
  }
  .footer-web span {
    position: absolute;
    right: 30px;
    top: 8px;
    font-size: 13px;
    color: #fff;
  }
</style>
</head>
<body>
  <main class="letterhead">
    <header class="brand">
      <div class="brand-square"></div>
      <div class="brand-name">VERTEX WORKS</div>
    </header>

    <p class="salutation">Dear Sir,</p>

    <p class="body-text p1">Lorem Ipsum is simply dummy text of the printing and typesetting industry. Lorem Ipsum has been the industry's standard dummy text ever since the 1500s, when an unknown printer took a galley of type and scrambled it to make a type specimen book. It has survived not only five centuries, but also the leap into electronic typesetting, remaining essentially unchanged. It was popularised in the 1960s with the release of Letraset sheets containing Lorem Ipsum passages, and more recently with desktop publishing software like Aldus PageMaker including versions of Lorem Ipsum.</p>

    <p class="body-text p2">Lorem Ipsum is simply dummy text of the printing and typesetting industry. Lorem Ipsum has been the industry's standard dummy text ever since the 1500s, when an unknown printer took a galley of type and scrambled it to make a type specimen book. It has survived not only five centuries, but also the leap into electronic typesetting, remaining essentially unchanged. It was popularised in the 1960s with the release of Letraset sheets containing Lorem Ipsum passages, and more recently with desktop publishing software like Aldus PageMaker including versions of Lorem Ipsum.</p>

    <p class="body-text p3">Lorem Ipsum is simply dummy text of the printing and typesetting industry. Lorem Ipsum has been the industry's standard dummy text ever since the 1500s, when an unknown printer took a galley of type and scrambled it to make a type specimen book.</p>

    <p class="sign-name">Nat Kip</p>
    <div class="signature" role="img" aria-label="Handwritten signature of Nat Kip"></div>
    <p class="sign-role">CEO &nbsp;|&nbsp; Owner</p>

    <footer>
      <div class="contact">
        <p>48 Harbour Lane, Westfield 6100</p>
        <div class="contact-line">
          <svg width="16" height="16" viewBox="0 0 16 16" aria-hidden="true">
            <circle cx="8" cy="8" r="7" fill="none" stroke="var(--brand-green)" stroke-width="1.2"/>
            <path d="M4.5 6.5 q3.5-2.5 7 0 l-0.8 1.2 h-1.3 v-0.9 h-2.8 v0.9 h-1.3z M5.5 8.5 h5 v2.5 h-5z" fill="var(--brand-green)"/>
          </svg>
          <span>08 5550 1234</span>
          <span class="gap"></span>
          <svg width="16" height="16" viewBox="0 0 16 16" aria-hidden="true">
            <circle cx="8" cy="8" r="7" fill="none" stroke="var(--brand-green)" stroke-width="1.2"/>
            <rect x="4.5" y="5.5" width="7" height="5" fill="var(--brand-green)"/>
            <path d="M4.5 5.5 L8 8.4 L11.5 5.5" fill="none" stroke="#fff" stroke-width="0.8"/>
          </svg>
          <span>info@vertexworks.com.au</span>
        </div>
      </div>
      <div class="footer-band"></div>
      <div class="footer-web">
        <svg width="280" height="36" viewBox="0 0 280 36" aria-hidden="true">
          <path d="M0 36 L12 10 Q17 0 30 0 L280 0 L280 36 Z" fill="var(--brand-blue)"/>
        </svg>
        <span>www.vertexworks.com.au</span>
      </div>
    </footer>
  </main>
</body>
</html>
```